Listing Presentation for The Larkspur Circle of Fenwick Realty

We need a unique listing presentation for homeowners interested in selling their home. The presentation should communicate our knowledge of the selling process, the market and our strengths as a real estate team. A cohesive look that conveys our belief of putting our clients and their families first.

Target Market(s)

Homeowners interested in selling their home

Industry/Entity Type

Real Estate

Font styles to use
Sans Serif

Colors
0255a3
9bcb3c

Requirements
Must have
• -color match those of our logo: #11214a #98EO61
• -template so we can add additional pages as needed

```html
<!DOCTYPE html>
<html lang="en">
<head>
<meta charset="utf-8">
<title>Listing Presentation – Inner Pages</title>
<link rel="stylesheet" href="https://fonts.googleapis.com/css2?family=Figtree:wght@400;500;700&family=Montserrat:wght@600;700&family=Tinos:wght@400;700&display=swap">
<style>
  :root {
    --navy: #11214a;
    --green: #98e061;
    --backdrop: #d4d4d4;
    --paper: #ffffff;
    --text: #1d2a55;
    --quote-grey: #6e7280;
    --line-green: #cfeeb6;
  }
  * { margin: 0; padding: 0; box-sizing: border-box; }
  html, body { width: 1200px; height: 1200px; overflow: hidden; }
  body {
    background: var(--backdrop);
    font-family: "Figtree", Arial, sans-serif;
    color: var(--text);
    position: relative;
  }
  .spread {
    position: absolute;
    left: 60px; top: 196px;
    width: 1086px; height: 768px;
    display: flex;
    background: var(--paper);
  }
  .page { position: relative; height: 100%; }
  .page--about { width: 542px; display: flex; }
  .page--reviews { width: 544px; }

  .about-column { position: relative; width: 298px; height: 100%; }
  .house-photo {
    width: 244px; height: 100%;
    background: linear-gradient(180deg, #2f5fb0 0%, #6d8fc6 22%, #b9b3a6 40%, #8b8578 62%, #a5a39e 78%, #7a7874 100%);
  }

  .brand {
    position: absolute;
    display: flex; align-items: center; gap: 7px;
    font-family: "Montserrat", Arial, sans-serif;
    font-weight: 700; font-size: 13px; color: var(--navy);
  }
  .brand-mark { width: 14px; height: 14px; background: var(--green); }
  .page--about .brand { left: 24px; top: 36px; }
  .page--reviews .brand { right: 24px; top: 36px; }

  .about-title {
    position: absolute; left: 24px; top: 140px;
    font-family: "Montserrat", Arial, sans-serif;
    font-size: 20px; font-weight: 700; color: var(--navy);
  }
  .about-body {
    position: absolute; left: 24px; top: 192px; width: 250px;
    font-size: 13.6px; line-height: 1.3; color: var(--text);
  }
  .about-body p { margin-bottom: 26px; }
  .about-body p:nth-child(2) { text-align: justify; }
  .about-body p:last-child { margin-bottom: 0; }

  .partner-name {
    position: absolute; left: 0; width: 298px; top: 666px;
    text-align: center;
    font-family: "Montserrat", Arial, sans-serif;
    font-weight: 700; font-size: 12px; color: var(--navy);
    letter-spacing: 0.5px;
  }

  .web-badge {
    position: absolute; bottom: 0;
    width: 222px; height: 48px;
    background: var(--green);
    display: flex; align-items: center; justify-content: center;
    font-family: "Tinos", "Times New Roman", serif;
    font-size: 16px; color: var(--navy);
  }
  .page--about .web-badge { left: 24px; }
  .page--reviews .web-badge { left: 294px; }

  .reviews-title {
    position: absolute; left: 70px; top: 82px;
    font-family: "Montserrat", Arial, sans-serif;
    font-size: 20px; font-weight: 700; color: var(--navy);
  }
  .reviews-source {
    position: absolute; left: 70px; top: 108px;
    font-size: 12.5px; color: var(--text);
  }

  .review-card {
    position: absolute; left: 52px; width: 436px;
    border: 1.5px solid var(--navy); border-radius: 22px;
    padding: 22px 24px 0 24px;
  }
  .review-card--first { top: 143px; height: 160px; }
  .review-card--second { top: 336px; height: 160px; }
  .review-card--third { top: 528px; height: 160px; }
  .review-text {
    position: relative;
    font-size: 13.2px; line-height: 1.28; text-align: justify; color: var(--text);
  }
  .quote-mark {
    position: absolute;
    font-family: "Tinos", serif; font-weight: 700;
    font-size: 44px; line-height: 1; color: var(--quote-grey);
  }
  .quote-mark--open { left: -22px; top: -8px; }
  .quote-mark--close { right: -18px; bottom: -30px; }
  .review-author {
    position: absolute; left: 0; right: 0;
    text-align: center; font-weight: 700; font-size: 13px; color: var(--navy);
  }
  .review-card--first .review-author { top: 124px; }
  .review-card--second .review-author { top: 130px; }
  .review-card--third .review-author { top: 120px; }

  .source-mark {
    position: absolute; left: 52px; bottom: 24px;
    display: flex; align-items: center; gap: 6px;
    font-family: "Montserrat", Arial, sans-serif;
    font-weight: 700; font-size: 19px; color: var(--navy);
  }
  .source-mark .brand-mark { width: 15px; height: 15px; }
  .footer-rule {
    position: absolute; left: 150px; right: 0; bottom: 28px;
    height: 1px; background: var(--line-green);
  }
</style>
</head>
<body>
  <div class="spread">
    <section class="page page--about">
      <div class="about-column">
        <div class="brand"><span class="brand-mark"></span>The Larkspur Circle</div>
        <h2 class="about-title">Fenwick Realty</h2>
        <div class="about-body">
          <p>Established in 2008, Fenwick Realty is a premier privately-owned real estate brokerage that has grown to include a roster of over 350 agents serving the Maryland, Washington D.C. and Virginia markets.</p>
          <p>Fenwick Realty is one of the fastest growing private owned residential real estate companies in the Mid-Atlantic, as named in 2016, 2017 and 2018 by Venture Monthly. Fenwick Realty falls in the top 3% of companies nationwide based on size, per the National Realty Council’s annual report.</p>
          <p>We provide maximum online exposure for our clients, with Fenwick Realty’s database of over 40 syndication partners. This allows our listings to appear on thousands of websites such as Searchly, Portal Homes, Homeview, Nestfinder, and even other real estate company websites.</p>
        </div>
        <div class="partner-name">FENWICK REALTY</div>
        <div class="web-badge">www.larkspurcircle.com</div>
      </div>
      <div class="house-photo" role="img" aria-label="Photograph of a tall Victorian townhouse with bay windows and a garage on a steep sloping street under a blue sky"></div>
    </section>

    <section class="page page--reviews">
      <div class="brand"><span class="brand-mark"></span>The Larkspur Circle</div>
      <h2 class="reviews-title">From our Satisfied Clients</h2>
      <p class="reviews-source">Homeview Reviews</p>

      <article class="review-card review-card--first">
        <p class="review-text"><span class="quote-mark quote-mark--open">“</span>Mr. Calloway made the sale of our home his top priority. We felt his genuine interest in our family’s objective to sell and relocate. He gave us excellent recommendations from prepping to pricing of our home. We had an offer within four days and confirmed the sale within a week. It was an excellent experience working with him.<span class="quote-mark quote-mark--close">”</span></p>
        <p class="review-author">-Jordan B.</p>
      </article>

      <article class="review-card review-card--second">
        <p class="review-text"><span class="quote-mark quote-mark--open">“</span>The thing that impressed me the most about Mr. Calloway was his being assertive while remaining kind and patient – his counsel is always honest, it makes everything move forward. I highly recommend his services.<span class="quote-mark quote-mark--close">”</span></p>
        <p class="review-author">-Elena M.</p>
      </article>

      <article class="review-card review-card--third">
        <p class="review-text"><span class="quote-mark quote-mark--open">“</span>Daniel and his team worked tirelessly to get me and my family into our dream home. He informed us what to expect and when to expect it. I would highly recommend.<span class="quote-mark quote-mark--close">”</span></p>
        <p class="review-author">-Marcus A.</p>
      </article>

      <div class="footer-rule"></div>
      <div class="source-mark"><span class="brand-mark"></span>Homeview</div>
      <div class="web-badge">www.larkspurcircle.com</div>
    </section>
  </div>
</body>
</html>
```